Ready mix concrete Company
Brennford Ready Mix, LLC
Project: Ready mix concrete Company
Ready mix concrete Company - Construction
Creative Brief
Professional
Ned Corvani
Owner
P.O. Box 846 Harlow Creek, NM. 88204
Ned.Corvani@mailvex.com
Colors are red, black, and white.
I have a logo...Not sure how to upload it here.

```html
<!DOCTYPE html>
<html lang="en">
<head>
<meta charset="utf-8">
<title>Brennford Ready Mix, LLC – Business Card</title>
<link href="https://fonts.googleapis.com/css2?family=Montserrat:wght@400;600;800&display=swap" rel="stylesheet">
<style>
  :root {
    --red: #e9383f;
    --black: #1d1d1f;
    --white: #ffffff;
    --stage: #ecebe8;
    --line: rgba(255,255,255,0.55);
  }
  * { box-sizing: border-box; margin: 0; padding: 0; }
  html, body { width: 1200px; height: 629px; overflow: hidden; }
  body {
    background: var(--stage);
    font-family: "Montserrat", Arial, sans-serif;
    display: flex;
    align-items: center;
    justify-content: center;
    gap: 60px;
  }
  .card {
    width: 520px;
    height: 300px;
    border-radius: 4px;
    box-shadow: 0 6px 18px rgba(0,0,0,0.18);
    overflow: hidden;
    position: relative;
  }

  /* Front */
  .card-front {
    background: var(--red);
    display: flex;
    align-items: center;
    justify-content: center;
  }
  .brand {
    display: flex;
    align-items: center;
    gap: 12px;
  }
  .brand-mark {
    width: 18px;
    height: 18px;
    background: var(--black);
    flex: none;
  }
  .brand-name {
    font-weight: 800;
    font-size: 22px;
    letter-spacing: 1px;
    text-transform: uppercase;
    white-space: nowrap;
  }
  .card-front .brand-name { color: var(--white); }

  /* Back */
  .card-back { background: var(--white); }
  .back-top {
    height: 44px;
    background: var(--red);
  }
  .back-logo {
    height: 112px;
    display: flex;
    align-items: center;
    justify-content: center;
  }
  .card-back .brand-mark { background: var(--red); }
  .card-back .brand-name { color: var(--black); font-size: 22px; }
  .back-details {
    position: absolute;
    left: 0; right: 0; bottom: 0;
    height: 144px;
    background: var(--red);
    display: flex;
    align-items: center;
    padding: 0 30px;
    color: var(--white);
  }
  .holder {
    flex: 1;
    text-align: right;
    padding-right: 22px;
    font-size: 10px;
    line-height: 1.55;
    white-space: nowrap;
  }
  .holder-name { font-weight: 800; font-size: 12px; }
  .holder-title { margin-bottom: 8px; font-weight: 600; }
  .divider {
    width: 1px;
    height: 104px;
    background: var(--line);
  }
  .contacts {
    flex: 1.25;
    list-style: none;
    padding-left: 18px;
    font-size: 9.5px;
    line-height: 1;
    white-space: nowrap;
  }
  .contacts li {
    display: flex;
    align-items: center;
    gap: 7px;
    margin: 5px 0;
  }
  .contacts svg { width: 11px; height: 11px; flex: none; }
</style>
</head>
<body>

  <section class="card card-front" aria-label="Card front">
    <div class="brand">
      <span class="brand-mark"></span>
      <span class="brand-name">Brennford Ready Mix, LLC</span>
    </div>
  </section>

  <section class="card card-back" aria-label="Card back">
    <div class="back-top"></div>
    <div class="back-logo">
      <div class="brand">
        <span class="brand-mark"></span>
        <span class="brand-name">Brennford Ready Mix, LLC</span>
      </div>
    </div>
    <div class="back-details">
      <div class="holder">
        <p class="holder-name">Ned Corvani</p>
        <p class="holder-title">Owner</p>
        <p>P.O. Box 846</p>
        <p>Harlow Creek, NM. 88204</p>
      </div>
      <div class="divider"></div>
      <ul class="contacts">
        <li>
          <svg viewBox="0 0 12 12"><circle cx="6" cy="6" r="6" fill="#fff"/><path d="M4 3.2l1 1.2-.6.8c.4.9 1.1 1.6 2 2l.8-.6 1.2 1-.6 1.1C5.6 8.6 3.4 6.4 3.3 4z" fill="#e9383f"/></svg>
          505-555-0142
        </li>
        <li>
          <svg viewBox="0 0 12 12"><circle cx="6" cy="6" r="6" fill="#fff"/><rect x="3.5" y="4.5" width="5" height="3.5" fill="#e9383f"/><rect x="4.5" y="3" width="3" height="1.5" fill="#e9383f"/></svg>
          505-555-0187
        </li>
        <li>
          <svg viewBox="0 0 12 12"><circle cx="6" cy="6" r="6" fill="#fff"/><rect x="4.3" y="2.6" width="3.4" height="6.8" rx=".6" fill="#e9383f"/></svg>
          505-555-0163
        </li>
        <li>
          <svg viewBox="0 0 12 12"><circle cx="6" cy="6" r="6" fill="#fff"/><rect x="3" y="4" width="6" height="4" fill="#e9383f"/><path d="M3 4l3 2.2L9 4" stroke="#fff" stroke-width=".7" fill="none"/></svg>
          Ned.Corvani@mailvex.com
        </li>
        <li>
          <svg viewBox="0 0 12 12"><circle cx="6" cy="6" r="6" fill="#fff"/><circle cx="6" cy="6" r="2.6" fill="#e9383f"/></svg>
          NedCorvani
        </li>
        <li>
          <svg viewBox="0 0 12 12"><circle cx="6" cy="6" r="6" fill="#fff"/><circle cx="6" cy="6" r="3" fill="none" stroke="#e9383f" stroke-width=".8"/><path d="M3 6h6M6 3v6" stroke="#e9383f" stroke-width=".7"/></svg>
          www.brennfordmix.com
        </li>
      </ul>
    </div>
  </section>

</body>
</html>
```